Local massage therapist needs some new marketing material

Hi there! I am a massage therapist here in Denver, CO in Brindle Hollow(shopping and art district) of the city. My business is called Lunora Massage of Denver. My practice has an eastern influence and I do reflexology, thai massage and use Chinese herbs, etc. I know all my clients and pay close attention to details. I am also very respectful of tradition and it shows in how I work. I tend to like modern, clean, fun, Asian designs. I am wanting a new business card and brochure. I have a logo and branding for my business that I want used in the design. Currently, the sign for my building is purple and I think my logo was designed to be purple. I will attach pictures of it and can send whatever files are necessary so it can be integrated into the brochure, etc. I like the purple but open to using other colors as well. Thanks!
My website is lunoramassagestudio.example where info can be gathered about me and services/fees for brochure.
Updates

Just increased budget. Please see new feedback in discussion thread.

Thanks!

                                       HEY ALL,

Just wanted to let you know that I made a change to my website. It is on the Prices Page. I no longer have the frequent  flyer prices but I added discounts. Let me know if you have any questions. Thanks so much!

Target Market(s)

healthy, urban, educated, upper middle class, yogis

Industry/Entity Type

Marketing

Requirements
Must have
• logo stays purple
Should not have
• not too busy

```html
<!DOCTYPE html>
<html lang="en">
<head>
<meta charset="utf-8">
<title>Lunora Massage of Denver – Brochure Inside</title>
<link href="https://fonts.googleapis.com/css2?family=Kalam:wght@700&family=Source+Sans+3:wght@400;600;700&display=swap" rel="stylesheet">
<style>
  :root{
    --purple:#5e2d91;
    --purple-deep:#4f2380;
    --green:#7dc242;
    --ink:#231f20;
    --paper:#ffffff;
    --stone-1:#9a9894;
    --stone-2:#5f5d59;
    --skin-1:#c89a7a;
    --skin-2:#7a5a44;
    --cut:#8a8a8a;
  }
  *{box-sizing:border-box;margin:0;padding:0}
  html,body{width:1200px;height:848px;overflow:hidden;background:var(--paper)}
  body{position:relative;font-family:"Source Sans 3",Arial,sans-serif;color:var(--ink)}

  .panel-label{position:absolute;left:18px;top:4px;font-family:"Kalam",cursive;font-size:30px;color:#222}
  .cut-mark{position:absolute;width:0;border-left:1px dashed var(--cut)}

  /* left panel */
  .price-panel{position:absolute;left:108px;top:47px;width:327px;height:521px;background:var(--purple);color:#fff;padding:18px 14px 0 14px;font-size:11px;line-height:17.5px}
  .price-panel h2{font-size:17px;font-weight:700;line-height:20px;margin-bottom:1px}
  .price-row{display:flex}
  .price-row .item{width:133px}
  .price-row.wide .item{width:auto;margin-right:6px}
  .price-note{line-height:15px;margin:2px 0 4px}
  .map{position:absolute;left:5px;top:334px;width:318px;height:174px;border:5px solid var(--green);background:linear-gradient(135deg,#e9e6df,#d9d6cf)}

  .brand{position:absolute;left:170px;top:594px;display:flex;align-items:center;gap:14px}
  .brand-name{font-size:40px;font-weight:400;letter-spacing:6px;color:var(--purple)}
  .contact{position:absolute;left:108px;top:662px;width:327px;text-align:center;color:var(--purple);font-weight:600;font-size:12px;line-height:20.5px}

  .footer-bar{position:absolute;top:783px;height:14px;background:var(--purple)}
  .footer-name{position:absolute;top:779px;font-size:17px;letter-spacing:3px;color:var(--purple);font-weight:400}

  /* header bands */
  .stone-band{position:absolute;top:47px;height:63px;background:linear-gradient(180deg,var(--stone-1),var(--stone-2))}
  .band-tag{position:absolute;top:64px;height:21px;background:var(--green);color:#fff;font-weight:700;font-size:12px;line-height:21px;padding-left:10px}

  /* columns */
  .column{position:absolute;font-size:12.5px;line-height:15.3px;text-align:justify}
  .column h2{font-size:28px;line-height:32px;font-weight:700;color:var(--purple);text-align:left}
  .column h3{font-size:12.5px;font-weight:700;line-height:15.3px;text-align:left}
  .photo{display:block}
  .float-spacer{float:right;width:0;height:28px}
  .float-photo{float:right;clear:right;margin-left:6px}
</style>
</head>
<body>
  <div class="panel-label">Inside</div>
  <div class="cut-mark" style="left:763px;top:0;height:40px"></div>
  <div class="cut-mark" style="left:1090px;top:0;height:40px"></div>
  <div class="cut-mark" style="left:763px;top:810px;height:38px"></div>
  <div class="cut-mark" style="left:1090px;top:810px;height:38px"></div>

  <section class="price-panel">
    <h2>Price List</h2>
    <p>Standard Prices</p>
    <div class="price-row"><span class="item">1 Hour Massage</span><span>$50</span></div>
    <div class="price-row"><span class="item">1-1/2 Hour Massage</span><span>$65</span></div>
    <div class="price-row"><span class="item">2 Hour Massage</span><span>$80</span></div>
    <div class="price-row wide"><span class="item">Add: Fire Cupping, Thai Herbal Compress or Reflexology</span><span>$10 each</span></div>
    <div class="price-row"><span class="item">Add: Hot Stones</span><span>$15</span></div>
    <div class="price-row"><span class="item">Cancellation Fee*</span><span>$25 for each hour booked</span></div>
    <p>Discounts</p>
    <p class="price-note">Massage Punch Card: Upon your initial visit, you will receive your first punch. After 9 massages at the regular price, you will earn a free 1 hour massage of your choice.</p>
    <p class="price-note">Referral Program: Get $10 off for every referral you make that comes in for a session. Gift certificates purchased for new clients will count toward the discount.</p>
    <p class="price-note">Seniors, Students &amp; Educators: Ask about your discount.</p>
    <p class="price-note">* 24 Hour Cancelation Policy applies to all Massage.</p>
    <p class="price-note">Prices are subject to change. Notice will be given.</p>
    <div class="map" role="img" aria-label="Street map showing the studio on E 2nd Ave near Brindle Hollow"></div>
  </section>

  <div class="brand">
    <span class="brand-name">LUNORA</span>
    <svg width="58" height="58" viewBox="0 0 58 58" aria-hidden="true"><circle cx="29" cy="29" r="26" fill="none" stroke="var(--purple)" stroke-width="2"/></svg>
  </div>

  <address class="contact" style="font-style:normal">
    Where We're Located<br>
    1487 E 2nd Ave, Denver, CO 80206<br>
    P: 303.555.0148<br>
    E: info@lunoramassagestudio.example<br>
    Tues - Fri 10am - 8pm Sat 10am-5pm<br>
    (Appointments required) No walk-ins please.
  </address>

  <div class="footer-bar" style="left:108px;width:492px"></div>
  <div class="footer-name" style="left:606px">LUNORA</div>
  <div class="footer-bar" style="left:763px;width:162px"></div>
  <div class="footer-name" style="left:932px">LUNORA</div>

  <div class="stone-band" role="img" aria-label="Photo of smooth river stones" style="left:437px;width:326px"></div>
  <div class="band-tag" style="left:450px;width:180px">GET TO KNOW YOUR THERAPIST.</div>
  <div class="stone-band" role="img" aria-label="Photo of smooth river stones" style="left:770px;width:320px"></div>
  <div class="band-tag" style="left:775px;width:177px">THE OPTIONS ARE ENDLESS</div>

  <section class="column" style="left:447px;top:120px;width:306px">
    <h2>Blend Massage</h2>
    <p>Blend Massage incorporates all techniques into one fully restorative and therapeutic session. Enjoy the benefits of soothing Swedish strokes, attention to Thai Sen lines, gentle stretching and deep pressure to relieve accumulated muscle tension and stress. This is the most popular modality.</p>
    <div class="photo" role="img" aria-label="Photo of a therapist massaging a client's back" style="width:128px;height:76px;margin:-10px 2px 0 auto;background:linear-gradient(135deg,var(--skin-1),var(--skin-2))"></div>
    <h2 style="margin-top:-16px">Prenatal Bliss</h2>
    <p><span class="float-spacer"></span><span class="float-photo" role="img" aria-label="Photo of an expectant mother relaxing on a massage table" style="width:148px;height:62px;background:linear-gradient(135deg,#e8dccd,#b99a80)"></span>Prenatal massage has been found to reduce stress, decrease swelling in the arms and legs, and relieve aches and pains in muscles and joints. Not only can massage be physically beneficial, but the human touch can be comforting and provide emotional support during pregnancy. Massage therapy has been found to reduce anxiety and depression. Massage is best to start during the second trimester.</p>
    <h2 style="margin-top:2px">Extra Massage Treats</h2>
    <h3 style="margin:2px 0 4px 4px">Chinese Fire Cupping:</h3>
    <p>Cupping Method that uses glass cups to create a vauum on the skin of the back. The suction penetrates deep into the tissues, allowing them to relax and release toxins. It triggers the lymphatic system, clears the blood vessels, loosens tight muscles, and stimulates the skin.</p>
    <div class="photo" role="img" aria-label="Photo of glass fire cups being placed on a client's back" style="width:216px;height:136px;margin:6px 0 0 45px;background:linear-gradient(135deg,#d8c2ae,#6a4f3d)"></div>
  </section>

  <section class="column" style="left:772px;top:118px;width:310px">
    <h3>Hot Stones:</h3>
    <p style="margin-top:5px">Hot stones (local basalt Colorado rocks) incorporates the use of smooth heated stones for a deeply soothing and relaxing experience. The stones are either used as part of a traditional swedish session or placed along specific areas of muscle tension to reduce discomfort and increase circulation. A nice treat after a long day or during the winter season.</p>
    <div style="display:flex;gap:9px;margin:3px 0 0 16px">
      <div role="img" aria-label="Photo of hot stones placed along a client's back" style="width:136px;height:122px;background:linear-gradient(135deg,var(--skin-1),var(--skin-2))"></div>
      <div role="img" aria-label="Photo of hands holding a smooth warm stone" style="width:132px;height:122px;background:linear-gradient(135deg,#e2c6ac,#9a7458)"></div>
    </div>
    <h3 style="margin-top:2px">Reflexology:</h3>
    <p style="margin-top:5px">A modality focused on the feet. It is a non-invasive way to work the entire body system. Pressure is applied to various reflexes on the foot in order to promote balance and healing in the body. Certain areas of the foot correspond to organs and specific parts of the body. Reflexology helps to clear blocked energy, balance emotions and relax the body.</p>
    <div role="img" aria-label="Photo of a warm herbal compress pressed on a relaxing client" style="width:237px;height:158px;margin:11px 0 0 36px;background:linear-gradient(135deg,#d9b07a,#7a5432)"></div>
    <h3 style="margin-top:10px">Thai Herbal Compress:</h3>
    <p style="margin-top:5px">Hand-made herbal compresses imported from Thailand make for a truly delightful and unique experience. The steamed herbal compress is applied directly to the body and helps relieve sore muscles while the aroma soothes the mind.</p>
  </section>
</body>
</html>
```